Healthy Meal Delivery Website needs a new face lift

Hi there,

The current website i have is super old and outdated.

I would like a beautiful modern site that has all the same content as the previous except with a a new, modern and trustworthy feel.

The current website is http://www.fennoxdinners.ca/

Target Market(s)

Diet Meal delivery, weight loss, healthy meal delivery

Industry/Entity Type

Food Service

Number of Pages Required

5+ page

Font styles to use
Sans Serif

Requirements
Must have
• Modern & Clean
Should not have
• Anything outdated or cheesy

```html
<!DOCTYPE html>
<html lang="en">
<head>
<meta charset="utf-8">
<title>Fennox Dinners — Great Tasting Diet Meal Delivery</title>
<link rel="stylesheet" href="https://fonts.googleapis.com/css2?family=Alegreya:wght@400;700&family=Open+Sans:ital,wght@0,400;0,600;0,700;0,800;1,400&display=swap">
<style>
:root{
  --blue:#29a8e0;
  --orange:#f7941d;
  --ink:#1b1b1b;
  --text:#444;
  --muted:#f2f2f2;
  --footer:#1c1c1c;
  --white:#fff;
  --serif:"Alegreya", Georgia, serif;
  --sans:"Open Sans", Arial, sans-serif;
}
*{box-sizing:border-box;margin:0;padding:0}
html,body{width:1200px;height:3169px;overflow:hidden}
body{position:relative;background:var(--white);font-family:var(--sans);color:var(--text)}

/* header */
.site-header{position:absolute;left:0;top:0;width:1200px;height:155px;background:var(--white)}
.brand{position:absolute;left:76px;top:48px;display:flex;align-items:center;gap:12px;font-family:var(--serif);font-weight:700;font-size:38px;color:var(--blue);line-height:1}
.brand-dot{width:26px;height:26px;border-radius:50%;background:var(--blue)}
.phone{position:absolute;left:938px;top:26px;display:flex;align-items:center;gap:14px;font-family:var(--serif);font-size:25px;color:var(--blue)}
.phone-ring{width:34px;height:34px;border-radius:50%;border:1.5px solid #bbb;display:flex;align-items:center;justify-content:center}
.main-nav{position:absolute;left:317px;width:809px;top:93px;display:flex;justify-content:space-between}
.main-nav a{display:block;height:42px;line-height:42px;padding:0 17px;font-family:var(--serif);font-size:15px;color:var(--ink);text-decoration:none;letter-spacing:.3px}
.main-nav a.is-active{background:var(--blue);color:var(--white)}

/* hero */
.hero{position:absolute;left:0;top:155px;width:1200px;height:538px;overflow:hidden}
.hero-photo{position:absolute;inset:0;background:
  radial-gradient(ellipse at 78% 40%, #b07a52 0%, #8a5a3a 25%, transparent 55%),
  radial-gradient(ellipse at 15% 80%, #3f6b2a 0%, transparent 50%),
  linear-gradient(100deg,#5d6f3e 0%,#8a8a6a 35%,#a48866 60%,#6e4b33 100%)}
.hero-shade{position:absolute;inset:0;background:rgba(0,0,0,.22)}
.hero h1{position:absolute;left:0;width:1200px;top:209px;text-align:center;font-weight:800;font-size:42px;color:var(--white);letter-spacing:.5px}
.hero p{position:absolute;left:0;width:1200px;top:275px;text-align:center;font-weight:700;font-size:28px;color:var(--white)}
.btn-order{position:absolute;left:509px;top:344px;width:180px;height:53px;line-height:53px;text-align:center;background:var(--orange);color:var(--white);font-family:var(--serif);font-size:19px;text-decoration:none}
.hero-arrow{position:absolute;top:252px;width:38px;height:38px;border:2px solid var(--white);border-radius:50%}
.hero-arrow svg{display:block}

/* intro */
.section-title{position:absolute;left:0;width:1200px;text-align:center;font-family:var(--serif);font-size:31px;color:var(--blue);letter-spacing:.5px;text-transform:uppercase;font-weight:400}
.section-title b{color:var(--ink);font-weight:400}
.intro-text{position:absolute;left:90px;top:810px;width:1020px;text-align:center;font-size:15.5px;line-height:29px;color:#555;letter-spacing:.2px}
.btn-dark{position:absolute;height:52px;line-height:52px;text-align:center;background:var(--ink);color:var(--white);font-family:var(--serif);font-size:16px;text-decoration:none;letter-spacing:.3px}

/* features */
.features{position:absolute;left:0;top:1042px;width:1200px;height:568px}
.features-photo{position:absolute;inset:0;background:
  radial-gradient(ellipse at 60% 40%, #4a3526 0%, transparent 60%),
  linear-gradient(180deg,#2b221c 0%,#3a2c22 50%,#241c17 100%)}
.feature{position:absolute;width:328px;height:188px;border:2px solid rgba(255,255,255,.55);background:rgba(0,0,0,.55);text-align:center;color:var(--white)}
.feature svg{position:absolute;left:50%;transform:translateX(-50%);top:24px}
.feature h3{position:absolute;left:0;width:100%;top:80px;font-family:var(--serif);font-weight:400;font-size:27px;color:var(--blue)}
.feature p{position:absolute;left:4px;width:316px;top:124px;font-size:14px;line-height:24px}

/* programs */
.program-photo{position:absolute;top:1741px;height:201px}
.program h3{position:absolute;top:1966px;text-align:center;font-family:var(--serif);font-weight:400;font-size:23px;color:var(--blue)}
.program p{position:absolute;top:2008px;text-align:center;font-size:13.5px;line-height:23px;color:#555;white-space:nowrap}

/* delivery */
.delivery{position:absolute;left:0;top:2246px;width:1200px;height:294px;background:var(--muted)}
.delivery-item{position:absolute;top:128px;width:260px;text-align:center}
.delivery-item svg{display:block;margin:0 auto}
.delivery-item span{display:block;margin-top:20px;font-family:var(--serif);font-size:19px;color:var(--ink)}

/* testimonials */
.quote{position:absolute;left:240px;width:720px;top:2644px;text-align:center;font-style:italic;font-size:18.5px;line-height:36px;color:#555}
.avatar{position:absolute;left:562px;top:2728px;width:76px;height:76px;border-radius:50%;background:radial-gradient(circle at 50% 40%,#b5654a 0%,#8c2f22 55%,#c8201e 100%)}
.quote-name{position:absolute;left:0;width:1200px;top:2812px;text-align:center;font-weight:700;font-size:15px;color:var(--ink)}
.quote-name em{font-style:normal;color:var(--blue)}
.chev{position:absolute;top:2728px}

/* footer */
.site-footer{position:absolute;left:0;top:2914px;width:1200px;height:255px;background:var(--footer);color:var(--white)}
.footer-brand{position:absolute;left:78px;top:60px;font-family:var(--serif);font-weight:700;font-size:32px;color:var(--blue)}
.copyright{position:absolute;left:76px;top:146px;font-size:12.5px;line-height:20px;color:#ddd}
.footer-head{position:absolute;top:52px;font-weight:700;font-size:13px;color:var(--blue);letter-spacing:.6px}
.footer-links{position:absolute;top:80px;list-style:none;font-size:14px;line-height:31px;color:#eee}
.contact-line{position:absolute;left:604px;display:flex;align-items:center;gap:14px;font-size:14px;color:#eee}
.newsletter-input{position:absolute;left:883px;top:91px;width:241px;height:48px;border:1.5px solid #ddd;padding-left:14px;line-height:45px;font-size:14px;color:#eee}
.btn-signup{position:absolute;left:1035px;top:154px;width:89px;height:36px;line-height:36px;text-align:center;background:var(--blue);color:var(--white);font-weight:700;font-size:12.5px;letter-spacing:.5px}
</style>
</head>
<body>

<header class="site-header">
  <div class="brand"><span class="brand-dot"></span>Fennox Dinners</div>
  <div class="phone">
    <span class="phone-ring"><svg width="16" height="16" viewBox="0 0 24 24"><path fill="#222" d="M6.6 10.8a15 15 0 0 0 6.6 6.6l2.2-2.2c.3-.3.7-.4 1-.2 1.1.4 2.3.6 3.6.6.6 0 1 .4 1 1V20c0 .6-.4 1-1 1A17 17 0 0 1 3 4c0-.6.4-1 1-1h3.5c.6 0 1 .4 1 1 0 1.3.2 2.5.6 3.6.1.3 0 .7-.2 1z"/></svg></span>
    416-555-0148
  </div>
  <nav class="main-nav">
    <a class="is-active" href="#">HOME</a><a href="#">HOW IT WORKS</a><a href="#">PRICING</a><a href="#">SAMPLE MENU</a><a href="#">CELEBRITY</a><a href="#">F.A.Q.</a><a href="#">CONTACT</a>
  </nav>
</header>

<section class="hero">
  <div class="hero-photo" role="img" aria-label="Grilled chicken breast on a bed of fresh salad greens"></div>
  <div class="hero-shade"></div>
  <h1>GREAT TASTING DIET MEAL DELIVERY</h1>
  <p>Diet meal delivery Toronto and Canada wide</p>
  <a class="btn-order" href="#">ORDER NOW</a>
  <span class="hero-arrow" style="left:61px"><svg width="34" height="34" viewBox="0 0 34 34"><path d="M19 10l-7 7 7 7" fill="none" stroke="#fff" stroke-width="2"/></svg></span>
  <span class="hero-arrow" style="left:1099px"><svg width="34" height="34" viewBox="0 0 34 34"><path d="M15 10l7 7-7 7" fill="none" stroke="#fff" stroke-width="2"/></svg></span>
</section>

<h2 class="section-title" style="top:752px">Fresh Diet Gourmet Meals Delivered <b>by the Fennox</b></h2>
<p class="intro-text">Fresh diet meal delivery Toronto and Canada wide is our signature fresh gourmet diet meal delivery program designed for healthy<br>living &amp; weight loss management.Diet meal delivery Toronto has a creative gourmet menu that uses exotic flavors and<br>ingredients to enhance your dining experience.</p>
<a class="btn-dark" href="#" style="left:509px;top:928px;width:182px">READ MORE</a>

<section class="features">
  <div class="features-photo" role="img" aria-label="Dark, softly blurred photo of plated gourmet dishes"></div>

  <div class="feature" style="left:76px;top:86px">
    <svg width="40" height="44" viewBox="0 0 40 44"><path fill="#fff" d="M6 2h18l10 10v30H6z"/><path fill="#222" d="M24 2v10h10z" opacity=".35"/><g stroke="#222" stroke-width="2.5"><path d="M12 22h16M12 28h16M12 34h16"/></g></svg>
    <h3>Benefits</h3><p>Fresh diet meal delivery daily</p>
  </div>
  <div class="feature" style="left:437px;top:86px">
    <svg width="40" height="48" viewBox="0 0 40 48"><g fill="#fff"><path d="M6 2h2v12h2V2h2v12h2V2h2v14a5 5 0 0 1-4 5v25h-4V21a5 5 0 0 1-4-5z"/><path d="M28 2c4 2 6 8 6 14v8h-3v22h-4V2z"/></g></svg>
    <h3>Menu</h3><p>Inspired fresh gourmet Fennox<br>Diet meals</p>
  </div>
  <div class="feature" style="left:797px;top:86px">
    <svg width="44" height="44" viewBox="0 0 44 44"><g fill="#fff"><circle cx="22" cy="8" r="3"/><path d="M4 32a18 18 0 0 1 36 0z"/><rect x="0" y="34" width="44" height="4" rx="2"/></g></svg>
    <h3>Variety</h3><p>60 Day Menu Rotation</p>
  </div>
  <div class="feature" style="left:76px;top:304px">
    <svg width="40" height="40" viewBox="0 0 40 40"><g stroke="#fff" stroke-width="3"><path d="M2 8h36M2 20h36M2 32h36"/></g><g fill="#fff"><rect x="22" y="3" width="6" height="10"/><rect x="8" y="15" width="6" height="10"/><rect x="18" y="27" width="6" height="10"/></g></svg>
    <h3>Customization</h3><p>Every fresh Fennox Diet meal is personally<br>customized</p>
  </div>
  <div class="feature" style="left:437px;top:304px">
    <svg width="48" height="40" viewBox="0 0 48 40"><g fill="#fff"><rect x="2" y="8" width="16" height="14"/><path d="M18 16h14l6 8H18z"/><circle cx="10" cy="32" r="6"/><circle cx="38" cy="32" r="6"/><path d="M30 4h6l2 12h-4z"/></g><circle cx="10" cy="32" r="2.5" fill="#222"/><circle cx="38" cy="32" r="2.5" fill="#222"/></svg>
    <h3>Delivery</h3><p>Fresh diet meal delivery daily Toronto<br>and Canada wide</p>
  </div>
  <div class="feature" style="left:797px;top:304px">
    <svg width="48" height="40" viewBox="0 0 48 40"><g fill="#fff"><ellipse cx="18" cy="15" rx="17" ry="12"/><path d="M6 24l-2 8 10-5z"/><ellipse cx="32" cy="24" rx="14" ry="10"/><path d="M40 31l4 7-10-4z"/></g></svg>
    <h3>Customer Service</h3><p>Personal Nutritionist available 7<br>days a week</p>
  </div>
</section>

<h2 class="section-title" style="top:1666px">Program Details</h2>

<div class="program">
  <div class="program-photo" style="left:76px;width:330px;background:radial-gradient(ellipse at 50% 55%,#a8461f 0%,#6a2a12 50%,#2a120a 100%)" role="img" aria-label="Roasted glazed chicken with herbs on a plate"></div>
  <h3 style="left:76px;width:330px">Enjoy Our Gourmet Menu</h3>
  <p style="left:76px;width:330px">Every fresh diet meal delivered is prepared<br>with the finest ingredients available and has a<br>creative menu that uses unique and exotic<br>flavors and ingredients..</p>
  <a class="btn-dark" href="#" style="left:151px;top:2124px;width:180px">READ MORE</a>
</div>
<div class="program">
  <div class="program-photo" style="left:433px;width:332px;background:linear-gradient(120deg,#d9e3e6 0%,#c9d3d4 45%,#b7b2a8 100%)" role="img" aria-label="Woman enjoying a meal in a bright room"></div>
  <h3 style="left:433px;width:332px">Customized For You</h3>
  <p style="left:433px;width:332px">The diet meal delivery program offers the<br>widest selection of healthy options regarding<br>your ingredients preference, allergies and<br>special requests.</p>
  <a class="btn-dark" href="#" style="left:509px;top:2124px;width:180px">READ MORE</a>
</div>
<div class="program">
  <div class="program-photo" style="left:797px;width:329px;background:radial-gradient(ellipse at 50% 55%,#c89a6a 0%,#8f7a4e 45%,#3e4a2a 100%)" role="img" aria-label="Fresh vegetable wrap cut in half"></div>
  <h3 style="left:797px;width:329px">Pause Your Program Anytime</h3>
  <p style="left:797px;width:329px">You are welcome to pause and restart your<br>meal program at anytime. Our customers lead<br>busy lives, therefore if you need to post-pone<br>a delivery let us know....</p>
  <a class="btn-dark" href="#" style="left:872px;top:2124px;width:180px">READ MORE</a>
</div>

<section class="delivery">
  <h2 class="section-title" style="top:46px">Delivery System</h2>
  <div class="delivery-item" style="left:64px">
    <svg width="50" height="60" viewBox="0 0 50 60"><path d="M17 16V10a8 8 0 0 1 16 0v6" fill="none" stroke="#29a8e0" stroke-width="3"/><path fill="#29a8e0" d="M4 16h42l-3 44H7z"/></svg>
    <span>What In Your Bag</span>
  </div>
  <div class="delivery-item" style="left:335px">
    <svg width="46" height="60" viewBox="0 0 46 60"><path fill="#29a8e0" d="M4 4h38v56H4z"/><path fill="#1a7fb0" d="M4 4h6v56H4z"/><text x="26" y="32" fill="#fff" font-family="Arial, sans-serif" font-size="10" text-anchor="middle">Menu</text><path d="M16 40h20M16 46h20" stroke="#fff" stroke-width="2"/></svg>
    <span>Your Daily Menu</span>
  </div>
  <div class="delivery-item" style="left:603px">
    <svg width="62" height="60" viewBox="0 0 62 60"><g fill="none" stroke="#29a8e0" stroke-width="7"><path d="M22 16l9-12 9 12"/><path d="M48 26l8 16H42"/><path d="M20 50H6l8-16"/></g><g fill="#29a8e0"><path d="M44 12l6 12-10 2z"/><path d="M38 42l-6 10-4-12z"/><path d="M6 26l10 6-8 6z"/></g></svg>
    <span>Recyclable Containers</span>
  </div>
  <div class="delivery-item" style="left:876px">
    <svg width="100" height="60" viewBox="0 0 100 60"><g fill="#29a8e0"><rect x="28" y="8" width="44" height="36"/><path d="M74 20h14l10 14v10H74z"/><circle cx="40" cy="50" r="8"/><circle cx="86" cy="50" r="8"/><rect x="4" y="14" width="18" height="3"/><rect x="10" y="24" width="14" height="3"/><rect x="0" y="34" width="22" height="3"/></g><circle cx="40" cy="50" r="3" fill="#f2f2f2"/><circle cx="86" cy="50" r="3" fill="#f2f2f2"/></svg>
    <span>Returning Your Cooler</span>
  </div>
</section>

<h2 class="section-title" style="top:2585px">Testimonials</h2>
<p class="quote">"I can train hard, eat well and feel great. Thank you FennoxDinners.ca for delivering such great food.""</p>
<div class="avatar" role="img" aria-label="Portrait of the customer"></div>
<p class="quote-name"><em>Mark Delaney</em> - Pro Hockey Player</p>
<svg class="chev" style="left:74px" width="24" height="30" viewBox="0 0 24 30"><path d="M18 3L6 15l12 12" fill="none" stroke="#555" stroke-width="3"/></svg>
<svg class="chev" style="left:1104px" width="24" height="30" viewBox="0 0 24 30"><path d="M6 3l12 12L6 27" fill="none" stroke="#555" stroke-width="3"/></svg>

<footer class="site-footer">
  <div class="footer-brand">Fennox Dinners</div>
  <p class="copyright">Copyright © 2018, Company Name<br>All Right Reserved</p>

  <h4 class="footer-head" style="left:344px">SITE MAP</h4>
  <ul class="footer-links" style="left:344px"><li>Home</li><li>How It Works</li><li>Pricing</li><li>Sample Menu</li></ul>
  <ul class="footer-links" style="left:478px"><li>Celebrity</li><li>F.A.Q.</li><li>Contact</li></ul>

  <h4 class="footer-head" style="left:604px">CONTACT US</h4>
  <div class="contact-line" style="top:81px"><svg width="14" height="14" viewBox="0 0 24 24"><path fill="#fff" d="M6.6 10.8a15 15 0 0 0 6.6 6.6l2.2-2.2c.3-.3.7-.4 1-.2 1.1.4 2.3.6 3.6.6.6 0 1 .4 1 1V20c0 .6-.4 1-1 1A17 17 0 0 1 3 4c0-.6.4-1 1-1h3.5c.6 0 1 .4 1 1 0 1.3.2 2.5.6 3.6.1.3 0 .7-.2 1z"/></svg>416-555-0148</div>
  <div class="contact-line" style="top:113px"><svg width="14" height="14" viewBox="0 0 24 24"><path fill="#fff" d="M2 5h20v14H2z"/><path d="M2 5l10 8 10-8" fill="none" stroke="#1c1c1c" stroke-width="2"/></svg>hello@fennoxdinners.ca</div>

  <h4 class="footer-head" style="left:883px">NEWSLETTER SIGN UP</h4>
  <div class="newsletter-input">Enter Email</div>
  <div class="btn-signup">SIGN UP</div>
</footer>

</body>
</html>
```